Verpackungen für Display Schutzglas
Vielen Dank für die tolle Zusammenarbeit, vom Anfang bis zum Ende war es uns eine Freude die Verpackung bzw. das Design zusammen zu gestalten.
Zielgruppe
Wir verkaufen Smartphone und Tabletzubehör. Für unseren Shop (Ladengeschäft) brauchen wir eine Verpackung für unser Display Schutzglas.
Aufgabenstellung
Wir möchten eine Verpackung die auf der Vorderseite sehr einfach gestaltet ist. Hier bitte nur auf das wesentliche hinweisen. Auf der Rückseite alles weitere wie Installation und Inhalt. Wir möchte einen Ausschnitt auf der Vorderseite durch den man den Inhalt erkennen kann. Bei den Farben bitte an die des Logos halten. Grundfarbe der Verpackung kann frei gewählt werden. Beispiel der Verpackung siehe jpg. Maße (BXH) 9,5 cm x 18 cm

```html
<!DOCTYPE html>
<html lang="de">
<head>
<meta charset="utf-8">
<title>Premium Displayschutz – Verpackung</title>
<link rel="stylesheet" href="https://fonts.googleapis.com/css2?family=Questrial&family=Roboto+Condensed:wght@300;700&display=swap">
<style>
  :root {
    --page: #ffffff;
    --panel-edge: #161616;
    --panel-mid: #3b3b3b;
    --lime: #b2c80c;
    --lime-text: #b6cc10;
    --ink: #1c1c1c;
    --white: #ffffff;
    --soft: #e8e8e8;
    --gold: #c9a23a;
    --gold-dark: #6e5214;
  }
  * { margin: 0; padding: 0; box-sizing: border-box; }
  html, body { width: 1200px; height: 1200px; overflow: hidden; background: var(--page); }
  body { position: relative; font-family: "Questrial", sans-serif; color: var(--soft); }

  .panel {
    position: absolute; top: 116px; width: 513px; height: 968px;
    background: radial-gradient(ellipse at 50% 45%, var(--panel-mid) 0%, #262626 55%, var(--panel-edge) 100%);
  }
  .panel--front { left: 78px; }
  .panel--back { left: 607px; }

  .brand {
    position: absolute; display: flex; align-items: center; gap: 12px;
    color: var(--white); font-family: "Questrial", sans-serif; line-height: 1; white-space: nowrap;
  }
  .brand__dot { width: 16px; height: 16px; border-radius: 50%; background: var(--lime); }
  .panel--front .brand { left: 0; width: 100%; justify-content: center; top: 92px; font-size: 40px; letter-spacing: 3px; }
  .panel--back .brand { left: 104px; top: 95px; font-size: 34px; letter-spacing: 3px; }

  .front__band {
    position: absolute; left: 0; top: 152px; width: 100%; height: 43px;
    background: var(--lime); color: var(--ink);
    font-size: 27px; letter-spacing: 12px; text-align: center; line-height: 43px; padding-left: 12px;
  }
  .front__title {
    position: absolute; left: 0; top: 206px; width: 100%; text-align: center;
    color: var(--white); font-family: "Roboto Condensed", sans-serif; font-weight: 300;
    font-size: 64px; line-height: 70px; letter-spacing: 0;
  }
  .front__photo {
    position: absolute; left: 40px; top: 278px; width: 470px; height: 580px;
    background: radial-gradient(ellipse at 55% 45%, #5a5a5a 0%, #2f2f2f 50%, rgba(30,30,30,0) 80%);
    border-radius: 30px;
  }
  .front__seal {
    position: absolute; left: 50px; top: 620px; width: 178px; height: 178px; border-radius: 50%;
    background: radial-gradient(circle at 40% 35%, #f1d77a 0%, var(--gold) 50%, var(--gold-dark) 100%);
  }
  .features { position: absolute; left: 131px; top: 869px; display: flex; }
  .feature { width: 56px; display: flex; flex-direction: column; align-items: center; }
  .feature svg { width: 28px; height: 28px; }
  .feature__label {
    margin-top: 5px; font-family: "Roboto Condensed", sans-serif; font-weight: 700;
    font-size: 10px; line-height: 11px; color: var(--white); text-align: center; white-space: nowrap;
  }

  .back__text {
    position: absolute; left: 104px; font-size: 16.5px; line-height: 24.7px;
    color: var(--soft); white-space: nowrap; letter-spacing: -0.3px;
  }
  .back__intro { top: 140px; }
  .back__highlight, .back__heading, .back__url {
    font-family: "Roboto Condensed", sans-serif; font-weight: 700; color: var(--lime-text);
    font-size: 17px; letter-spacing: 0;
  }
  .back__highlight { position: absolute; left: 104px; top: 312px; line-height: 24.7px; white-space: nowrap; }
  .steps { position: absolute; left: 104px; top: 387px; list-style: none; }
  .steps__heading { line-height: 24.7px; }
  .steps li { display: flex; font-size: 16.5px; line-height: 24.7px; white-space: nowrap; letter-spacing: -0.3px; }
  .steps__num { width: 24px; flex: none; font-family: "Roboto Condensed", sans-serif; font-weight: 700; color: var(--white); letter-spacing: 0; }
  .step-icon { position: absolute; left: 52px; }
  .back__delivery { top: 757px; }
  .back__url { position: absolute; left: 104px; top: 856px; }
</style>
</head>
<body>

<section class="panel panel--front">
  <div class="brand"><span class="brand__dot"></span><span>Lumenta</span></div>
  <div class="front__band">PREMIUM</div>
  <h1 class="front__title">DISPLAYSCHUTZ</h1>
  <div class="front__photo" role="img" aria-label="Foto: Hand hält ein Smartphone, darüber schwebt ein transparentes Schutzglas"></div>
  <div class="front__seal" role="img" aria-label="Goldenes Qualitätssiegel"></div>

  <div class="features">
    <div class="feature">
      <svg viewBox="0 0 28 28" fill="none" stroke="#fff" stroke-width="1.6"><rect x="2" y="2" width="24" height="24" rx="3"/><path d="M8 20 L20 8 M8 8 L14 14 M17 17 L20 20"/></svg>
      <span class="feature__label">Bruch &amp;<br>Kratzerschutz</span>
    </div>
    <div class="feature">
      <svg viewBox="0 0 28 28" fill="none" stroke="#fff" stroke-width="1.6"><rect x="2" y="2" width="24" height="24" rx="3"/><path d="M7 19 L11 9 M12 19 L16 9 M17 19 L21 9"/></svg>
      <span class="feature__label">Kratzfest</span>
    </div>
    <div class="feature">
      <svg viewBox="0 0 28 28" fill="none" stroke="#fff" stroke-width="1.6"><rect x="2" y="2" width="24" height="24" rx="3"/><path d="M6 14 Q14 6 22 14 Q14 22 6 14 Z"/><circle cx="14" cy="14" r="2.5"/></svg>
      <span class="feature__label">Unsichtbar</span>
    </div>
    <div class="feature">
      <svg viewBox="0 0 28 28" fill="none" stroke="#fff" stroke-width="1.6"><rect x="2" y="2" width="24" height="24" rx="3"/><path d="M10 12 Q7 17 10 19 Q13 17 10 12 Z M18 8 Q15 13 18 15 Q21 13 18 8 Z M17 17 Q14 21 17 23 Q20 21 17 17 Z"/></svg>
      <span class="feature__label">Schutz vor<br>Spritzwasser</span>
    </div>
  </div>
</section>

<section class="panel panel--back">
  <div class="brand"><span class="brand__dot"></span><span>Lumenta</span></div>

  <p class="back__text back__intro">Durch die Passgenauigkeit und Klarheit des<br>Premium Glasschutzes wird die<br>Berührungsempfindlichkeit deines Smartphones<br>nicht beeinträchtigt. Das Glas schützt dein<br>Smartphone bei Stürzen, Stößen oder vor<br>Kratzern durch seine extreme Härte.</p>

  <p class="back__highlight">9H Härtegrad, 2.5 D abgerundete Kanten,<br>rückstandslos entfernbar</p>

  <svg class="step-icon" style="top:412px" width="34" height="44" viewBox="0 0 34 44" fill="none"><rect x="1" y="1" width="24" height="40" rx="3" stroke="#fff" stroke-width="1.6"/><path d="M16 10 l2 4 4 2 -4 2 -2 4 -2-4 -4-2 4-2z M26 20 l1 2 2 1 -2 1 -1 2 -1-2 -2-1 2-1z" fill="var(--lime)"/></svg>
  <svg class="step-icon" style="top:488px" width="28" height="44" viewBox="0 0 28 44" fill="none"><rect x="1" y="1" width="24" height="40" rx="2" stroke="#fff" stroke-width="1.6"/><path d="M10 40 L24 26 L24 40 Z" fill="var(--lime)"/></svg>
  <svg class="step-icon" style="top:564px" width="30" height="48" viewBox="0 0 30 48" fill="none"><rect x="1" y="1" width="26" height="44" rx="3" fill="var(--lime)"/><rect x="5" y="6" width="18" height="32" rx="2" stroke="#fff" stroke-width="1.6"/></svg>
  <svg class="step-icon" style="top:614px" width="30" height="44" viewBox="0 0 30 44" fill="none"><rect x="1" y="1" width="26" height="40" rx="3" fill="var(--lime)" stroke="#fff" stroke-width="1.4"/><circle cx="14" cy="20" r="7" stroke="#fff" stroke-width="1.6"/><circle cx="14" cy="20" r="3" fill="#fff"/></svg>
  <svg class="step-icon" style="top:684px" width="30" height="44" viewBox="0 0 30 44" fill="none"><rect x="1" y="1" width="24" height="40" rx="3" fill="var(--lime)"/><circle cx="8" cy="8" r="2" fill="#fff"/><circle cx="16" cy="12" r="1.5" fill="#fff"/><rect x="12" y="20" width="14" height="9" transform="rotate(-15 19 24)" fill="#fff"/></svg>

  <ol class="steps">
    <li class="back__heading steps__heading">Kurzanleitung Installation:</li>
    <li><span class="steps__num">1</span><span>Reinige dein Display gründlich.<br>(Tücher befinden sich in der Packung)</span></li>
    <li><span class="steps__num">2</span><span>Entferne Staub mit dem beigefügten Aufkleber</span></li>
    <li><span class="steps__num">3</span><span>Nun die Folie vom Displayschutz vorsichtig<br>entfernen und dabei jeglichen Kontakt zur<br>Unterseite vermeiden</span></li>
    <li><span class="steps__num">4</span><span>Richte den Displayschutz auf deinem<br>Smartphone aus.</span></li>
    <li><span class="steps__num">5</span><span>Drücke nun den Displayschutz in der Mitte an<br>dein Smartphone. Premium Displayschutz<br>fixiert sich automatisch.</span></li>
    <li><span class="steps__num">6</span><span>Entferne mit der beigefügten Rakel kleine<br>Blasen.</span></li>
  </ol>

  <div class="back__text back__delivery">
    <p class="back__heading">Lieferumfang:</p>
    <p>Premium Displayschutz, Reinigungstuch,<br>Trockentuch, Staubsammelaufkleber, Rakel</p>
  </div>

  <p class="back__url">www.lumenta-zubehoer.de</p>
</section>

</body>
</html>
```